Anzeigengestaltung für Ankauf von Restposten und Konkurswaren und Verkauf auf eigener Auktionsplattform
Zielgruppe
Ankauf von Restposten und Konkurswaren. Verkauf auf unserer eigenen Auktionsplattform
Aufgabenstellung
Wir möchten ein cooles Design dass etwas hervorsticht. Das Design soll für Zeitungsinserate und Strassenbanner dienen. Ich habe mal Leienhaft im Paint etwas erstellt damit du siehst was alles drauf soll. Die beiden Logos 'Talmo' und 'Morvel' dürfen nicht verändert werden. Talmo Logo soll im helleren blau sein.

```html
<!DOCTYPE html>
<html lang="de">
<head>
<meta charset="utf-8">
<title>Talmo Liquidationen – Inserat</title>
<link rel="stylesheet" href="https://fonts.googleapis.com/css2?family=Lato:wght@300;400;700;900&display=swap">
<style>
  :root {
    --page: #ececec;
    --paper: #ffffff;
    --frame: #111111;
    --brand-blue: #1d5aa6;
    --band-grey: #58595b;
    --band-text: #f1f1f1;
    --accent-blue: #1a94c9;
    --ink: #141414;
    --white: #ffffff;
  }
  * { margin: 0; padding: 0; box-sizing: border-box; }
  html, body {
    width: 1200px;
    height: 815px;
    overflow: hidden;
    background: var(--page);
    font-family: "Lato", sans-serif;
  }
  .ad {
    position: absolute;
    left: 40px;
    top: 100px;
    width: 1120px;
    height: 615px;
    background: var(--paper);
    border: 3px solid var(--frame);
    overflow: hidden;
  }
  .ad-shapes {
    position: absolute;
    inset: 0;
  }
  .brand {
    position: absolute;
    left: 70px;
    top: 62px;
    display: flex;
    align-items: center;
    gap: 18px;
  }
  .brand-mark {
    width: 58px;
    height: 58px;
    background: var(--brand-blue);
  }
  .brand-text {
    padding-left: 16px;
    border-left: 1px solid var(--band-grey);
  }
  .brand-name {
    display: block;
    font-size: 70px;
    font-weight: 900;
    color: var(--brand-blue);
    letter-spacing: 2px;
    line-height: 0.9;
  }
  .brand-suffix {
    display: block;
    margin-top: 4px;
    font-size: 27px;
    font-weight: 300;
    color: var(--brand-blue);
    letter-spacing: 3px;
    line-height: 1;
  }
  .contact {
    position: absolute;
    left: 110px;
    top: 232px;
    font-size: 22px;
    line-height: 32px;
    color: var(--ink);
    font-style: normal;
  }
  .services {
    list-style: none;
  }
  .services li {
    position: absolute;
    font-size: 27px;
    font-weight: 700;
    color: var(--band-text);
    letter-spacing: 1.5px;
    white-space: nowrap;
    line-height: 1;
  }
  .platform {
    position: absolute;
    left: 897px;
    top: 392px;
    transform: translateX(-50%);
    text-align: center;
    color: var(--white);
    font-weight: 700;
    white-space: nowrap;
  }
  .platform-claim {
    font-size: 22px;
    line-height: 32px;
  }
  .platform-name {
    margin-top: 6px;
    font-size: 56px;
    font-weight: 900;
    line-height: 1;
    letter-spacing: -1px;
  }
</style>
</head>
<body>
  <section class="ad">
    <svg class="ad-shapes" width="1120" height="615" viewBox="0 0 1120 615" aria-hidden="true">
      <polygon class="service-band" points="620,0 990,0 700,615 290,615" fill="var(--band-grey)"/>
      <polygon class="platform-triangle" points="870,300 1117,615 722,615" fill="var(--accent-blue)"/>
    </svg>

    <div class="brand">
      <span class="brand-mark"></span>
      <div class="brand-text">
        <span class="brand-name">TALMO</span>
        <span class="brand-suffix">LIQUIDATIONEN</span>
      </div>
    </div>

    <address class="contact">
      Weidgasse 14<br>
      8842 Unteriberg<br>
      +41 (0)55 000 12 34<br>
      info@talmo-liq.ch
    </address>

    <ul class="services">
      <li style="left:525px; top:185px;">GESCHÄFTSAUFLÖSUNG</li>
      <li style="left:492px; top:245px;">RESTPOSTENHANDEL</li>
      <li style="left:460px; top:305px;">VERWERTUNG</li>
      <li style="left:428px; top:365px;">WOHNUNGSRÄUMUNG</li>
      <li style="left:396px; top:425px;">ENTSORGUNG</li>
    </ul>

    <div class="platform">
      <p class="platform-claim">mit<br>eigener<br>Online-<br>Auktionsplattform</p>
      <p class="platform-name">morvel.ch</p>
    </div>
  </section>
</body>
</html>
```